| ■お仕事内容 海外の高級ファッションブランドを販売するサイト用の無償修理保証のバナー製作をお願いいたします。 メンズ、レディースどちらも取り扱っているブランドのため、どちらでも使えるデザインが望ましいです。 ■バナーに記載する内容 「1年間無償修理保証」ということが伝わる文章を入れてください。 ※独自のサービスのため、「当店だけの・・・」など独自の付加価値サービスである文言を入れたいです。 ■重視する点 ・高級感のあるデザイン(ごちゃごちゃしていない、シンプルで目を引くもの) ・フラットデザインが基調になっているサイトにマッチするデザイン ・ファッション系のサイトに合うデザイン ・本物である安心感・信頼感のあるデザイン ■報酬 5,000円 ■応募条件 WEBサイトのバナー、アイコンなどの製作経験をお持ちの方 ご提案価格と実績のバランスを見てお仕事をお願いする方を選定させていただきます。 たくさんのご応募お待ちしております。 何卒宜しくお願いいたします。 |

```html
<!DOCTYPE html>
<html lang="ja">
<head>
<meta charset="UTF-8">
<title>当店だけ 1年間無償修理保証</title>
<link rel="stylesheet" href="https://fonts.googleapis.com/css2?family=Noto+Serif+JP:wght@900&family=Noto+Sans+JP:wght@900&display=swap">
<style>
  :root {
    --gold-deep: #8c6d2c;
    --gold-mid: #c9a75a;
    --gold-light: #f4e6bd;
    --gold-shine: #fffaf0;
    --ink: #1a1611;
    --badge: #0d0c0b;
    --white: #ffffff;
  }
  html, body {
    margin: 0;
    padding: 0;
    width: 1200px;
    height: 188px;
    overflow: hidden;
    background: var(--white);
  }
  .warranty-banner {
    position: relative;
    width: 1200px;
    height: 188px;
    overflow: hidden;
  }
  .satin-backdrop {
    position: absolute;
    inset: 0;
    background:
      linear-gradient(100deg, transparent 0%, rgba(255,250,235,0.0) 18%, rgba(255,250,235,0.75) 26%, transparent 34%),
      linear-gradient(75deg, transparent 42%, rgba(255,248,225,0.7) 52%, transparent 60%),
      linear-gradient(110deg, transparent 62%, rgba(120,90,35,0.35) 70%, rgba(255,245,220,0.8) 80%, transparent 90%),
      linear-gradient(180deg, var(--gold-light) 0%, var(--gold-mid) 45%, var(--gold-deep) 100%);
  }
  .exclusive-badge {
    position: absolute;
    left: 82px;
    top: 24px;
    width: 140px;
    height: 140px;
  }
  .exclusive-badge svg {
    position: absolute;
    inset: 0;
  }
  .badge-label {
    position: absolute;
    inset: 0;
    display: flex;
    flex-direction: column;
    align-items: center;
    justify-content: center;
    font-family: "Noto Sans JP", sans-serif;
    font-weight: 900;
    font-size: 24px;
    line-height: 1.15;
    color: var(--white);
    letter-spacing: 1px;
  }
  .warranty-headline {
    position: absolute;
    left: 270px;
    top: 50%;
    transform: translateY(-52%);
    margin: 0;
    font-family: "Noto Serif JP", serif;
    font-weight: 900;
    font-size: 64px;
    letter-spacing: 22px;
    color: var(--ink);
    white-space: nowrap;
    text-shadow:
      0 0 2px var(--gold-shine),
      0 0 4px var(--gold-shine),
      0 0 6px var(--gold-shine),
      2px 2px 3px var(--gold-shine);
  }
</style>
</head>
<body>
  <div class="warranty-banner">
    <div class="satin-backdrop" role="img" aria-label="光沢のあるゴールドのサテン生地の背景"></div>

    <div class="exclusive-badge">
      <svg viewBox="0 0 140 140" width="140" height="140" aria-hidden="true">
        <rect x="25" y="25" width="90" height="90" fill="var(--badge)"/>
        <rect x="25" y="25" width="90" height="90" fill="var(--badge)" transform="rotate(45 70 70)"/>
      </svg>
      <div class="badge-label">
        <span>当店</span>
        <span>だけ</span>
      </div>
    </div>

    <h1 class="warranty-headline">１年間無償修理保証</h1>
  </div>
</body>
</html>
```